Criminal Defense Law Firm needs Stationary design Theme for a Business Card, Envelope, and Letterhea

Our Law Firm is seeking a general design concept for a business card, letterhead, and Envelope.

Our website is WillowcrestTrialDesk.com

A design for these three items is requested to keep branding in place for the firm. Would like to keep the Firm Colors on the website consistent with our branding on business cards, letterheads, and mailing envelopes #10 size to be exact.

We would like business cards printed front and back with Law firm Colors from website.

Letterhead with law firm colors as well. Design is not limited to just the header, but the footer can be utilized as well for email, website, phone, fax, etc.

Simple #10 envelope consisting of the same design principles set out in the previous two designs.

```html
<!DOCTYPE html>
<html lang="en">
<head>
<meta charset="utf-8">
<title>Willowcrest Trial Desk – Business Card</title>
<link rel="stylesheet" href="https://fonts.googleapis.com/css2?family=Cormorant+Garamond:wght@500&family=Open+Sans:wght@300;700&display=swap">
<style>
  :root {
    --backdrop: #2a2a2a;
    --card: #161616;
    --card-edge: #2c2c2c;
    --silver: #e6e6e6;
    --silver-soft: #c9c9c9;
  }
  html, body {
    margin: 0;
    width: 1200px;
    height: 720px;
    overflow: hidden;
    background: var(--backdrop);
  }
  .stage {
    width: 1200px;
    height: 720px;
    display: flex;
    align-items: center;
    justify-content: center;
  }
  .business-card {
    position: relative;
    width: 840px;
    height: 480px;
    background: var(--card);
    border: 1px solid var(--card-edge);
    box-sizing: border-box;
    color: var(--silver);
  }
  .firm-mark {
    position: absolute;
    left: 64px;
    top: 104px;
    display: flex;
    align-items: center;
    gap: 22px;
  }
  .firm-mark__dot {
    width: 56px;
    height: 56px;
    border: 2px solid var(--silver);
    border-radius: 50%;
    box-sizing: border-box;
    flex: none;
  }
  .firm-mark__name {
    font-family: "Cormorant Garamond", Georgia, serif;
    font-weight: 500;
    font-size: 25px;
    line-height: 1.02;
    letter-spacing: 0.06em;
    text-transform: uppercase;
    color: var(--silver);
  }
  .attorney-name {
    position: absolute;
    left: 64px;
    top: 286px;
    margin: 0;
    font-family: "Open Sans", Arial, sans-serif;
    font-size: 31px;
    font-weight: 300;
    letter-spacing: 0.01em;
    text-transform: uppercase;
  }
  .attorney-name__surname { font-weight: 700; }
  .contact-list {
    position: absolute;
    left: 64px;
    top: 350px;
    margin: 0;
    padding: 0;
    list-style: none;
    font-family: "Open Sans", Arial, sans-serif;
    font-size: 19px;
    line-height: 30px;
    color: var(--silver-soft);
  }
  .contact-list__label {
    font-weight: 700;
    color: var(--silver);
    text-transform: uppercase;
  }
  .contact-list__value { font-weight: 300; }
</style>
</head>
<body>
  <main class="stage">
    <article class="business-card">
      <div class="firm-mark">
        <span class="firm-mark__dot" aria-hidden="true"></span>
        <div class="firm-mark__name">Willowcrest Trial Desk<br>Offices</div>
      </div>
      <h1 class="attorney-name">Owen <span class="attorney-name__surname">Halvorsen</span></h1>
      <ul class="contact-list">
        <li><span class="contact-list__label">Office.</span> <span class="contact-list__value">2417 Larkspur Avenue NW Millbrook, NM 87000</span></li>
        <li><span class="contact-list__label">Phone.</span> <span class="contact-list__value">505.555.0148</span></li>
      </ul>
    </article>
  </main>
</body>
</html>
```